Bright Towns Alliance PowerPoint Design Template and Sample Deck

The Bright Towns Alliance is an international organization that seeks to improve the livability, workability and sustainability of the world’s cities.
We seek a versatile PowerPoint design template with 10 slide types plus a “self-documenting” sample deck. Your design will be used in keynote speeches and workshops around the world.
After the contest is completed, we will ask the winning designer to add 10-20 additional slide types for $75 per slide. We also seek a long-term relationship whereby we can request “custom” slides and/or ask the designer to touch up the slides we build to make them better.
FILES. We have uploaded several files:
1. BRIGHT TOWNS ALLIANCE DESIGN CONTEST NOTES.docx with full instructions.
2. PALETTE. Shows our official colors.
3 LOGOS. Several individual files with different variations of our logo. Some with our motto, some without.
2. SAMPLE SLIDES. Because we were unable to successfully upload our sample deck, we are making it available via this FileCrate link:
https://www.filecrate-example.net/s/k7qvmr2tn8wzd4h/The%20Bright%20Towns%20Alliance%20Design%20Contest%20Notes.docx?dl=0
Target Market(s)
Mayors, department heads, CIOs, senior executives from technology companies
Industry/Entity Type
Information Technology
Colors
Designer to choose colors to be used in the design.
Requirements
Must have
- Please see uploaded Word document for requirements, nice to haves and should not haves and uploaded palette for color preferences.
Nice to have
- see above
Should not have
- see above

```html
<!DOCTYPE html>
<html lang="en">
<head>
<meta charset="utf-8">
<title>Bright Towns Alliance – Slide Template Set</title>
<link href="https://fonts.googleapis.com/css2?family=Raleway:wght@300;400;600;700&display=swap" rel="stylesheet">
<style>
:root{
  --blue:#5b82c8;
  --orange:#ee7a22;
  --ink:#333;
  --soft:#555;
  --chip:#efefef;
  --page:#ffffff;
}
*{box-sizing:border-box;margin:0;padding:0}
html,body{width:900px;height:1200px;overflow:hidden;background:var(--page)}
body{position:relative;font-family:"Raleway",sans-serif;color:var(--ink);font-weight:300}
.slide{position:absolute;width:418px;height:236px;background:#fff;overflow:hidden;
  box-shadow:2px 3px 5px rgba(0,0,0,.45);border:1px solid #eee}
.abs{position:absolute}
.brand-stack{position:absolute;font-size:16px;line-height:15px;color:var(--ink);font-weight:400}
.brand-line{position:absolute;font-size:14px;color:var(--ink);font-weight:400;right:12px}
.hline{position:absolute;height:1.5px;background:var(--blue)}
.vline{position:absolute;width:1.5px;background:var(--blue)}
.photo{position:absolute}

/* agenda */
.agenda .num{position:absolute;left:94px;width:19px;height:19px;background:var(--chip);font-size:9px;font-weight:600;display:flex;align-items:center;justify-content:center}
.agenda .label{position:absolute;left:121px;width:149px;height:19px;background:var(--chip);font-size:10px;padding-left:7px;line-height:19px}
.agenda .active.num,.agenda .active.label{background:var(--blue);color:#fff}
.agenda .big-num{position:absolute;left:332px;top:-8px;font-size:84px;font-weight:400;color:var(--blue);line-height:1}

/* quote */
.quote-text{position:absolute;left:40px;width:338px;top:58px;text-align:center;font-size:14px;line-height:17px;color:var(--ink)}
.quote-by{position:absolute;left:0;width:418px;top:150px;text-align:center;font-size:8px;color:var(--soft)}

/* bullets */
.side-title{position:absolute;left:189px;top:18px;font-size:14px;line-height:17px;color:var(--orange);font-weight:300}
.side-list{position:absolute;left:189px;top:66px;list-style:none}
.side-list li{font-size:8.5px;height:21px;display:flex;align-items:center;gap:6px;color:var(--ink)}
.side-list li::before{content:"";width:7px;height:7px;background:var(--orange)}

/* columns */
.col{position:absolute;top:82px;width:80px;text-align:center;font-size:12px;line-height:14.5px;color:var(--soft);transform:translateX(-50%)}
.tag{position:absolute;right:24px;top:182px;font-size:11px;font-weight:700;color:var(--blue);letter-spacing:.3px}

/* appeal */
.appeal{position:absolute;right:166px;top:30px;text-align:right;font-size:19px;line-height:23px;color:var(--ink)}
.appeal b{color:var(--blue);font-weight:700}

/* market */
.stat{position:absolute;width:172px;height:86px;border:1.5px solid var(--orange)}
.stat .fig{position:absolute;left:4px;top:2px;font-size:22px;font-weight:700;color:var(--orange)}
.stat .fig small{font-size:8px;color:var(--ink);font-weight:400;margin-left:4px}
.stat .when{position:absolute;right:5px;top:3px;font-size:8px;color:var(--soft)}
.stat ul{position:absolute;left:16px;top:50px;font-size:7.5px;line-height:10px;color:var(--soft)}
.stat li{margin-bottom:2px}
.sheet-title{position:absolute;left:18px;top:207px;font-size:14px;font-weight:600;color:var(--blue);letter-spacing:.3px}
</style>
</head>
<body>

<!-- agenda -->
<section class="slide agenda" style="left:20px;top:26px">
  <div class="hline" style="left:0;top:35px;width:84px"></div>
  <div class="hline" style="left:276px;top:35px;width:44px"></div>
  <div class="hline" style="left:380px;top:35px;width:38px"></div>
  <div class="big-num">1</div>
  <div class="num active" style="top:24px">1</div><div class="label active" style="top:24px">Lorem Ipsum</div>
  <div class="num" style="top:57px">2</div><div class="label" style="top:57px">Lorem Ipsum</div>
  <div class="num" style="top:90px">3</div><div class="label" style="top:90px">Lorem Ipsum</div>
  <div class="num" style="top:123px">4</div><div class="label" style="top:123px">Lorem Ipsum</div>
  <div class="num" style="top:156px">5</div><div class="label" style="top:156px">Lorem Ipsum</div>
  <div class="num" style="top:189px">6</div><div class="label" style="top:189px">Lorem Ipsum</div>
  <div class="brand-stack" style="left:10px;top:180px">Bright<br>Towns<br>Alliance</div>
</section>

<!-- race -->
<section class="slide" style="left:462px;top:26px">
  <div class="abs" style="left:18px;top:34px;font-size:14px">It’s not just a trend, it’s a <b style="color:var(--orange);font-weight:700">race</b></div>
  <div class="photo" role="img" aria-label="Road over an arched steel bridge at sunrise" style="left:0;top:60px;width:418px;height:144px;background:linear-gradient(180deg,#6f8aa6 0%,#9fb0bd 40%,#f4b23a 62%,#5a3a20 80%,#2a2422 100%)"></div>
  <div class="abs" style="left:0;top:59px;width:418px;height:1.5px;background:var(--orange)"></div>
  <div class="abs" style="left:0;top:204px;width:418px;height:1.5px;background:var(--orange)"></div>
  <div class="brand-line" style="top:212px">Bright Towns Alliance</div>
</section>

<!-- quote -->
<section class="slide" style="left:18px;top:276px">
  <p class="quote-text">"Lorem ipsum dolor sit amet, consetetur sadipscing elitr, sed diam nonumy eirmod tempor invidunt ut labore et dolore magna aliquyam erat, sed diam voluptua."</p>
  <p class="quote-by">- At vero eos et accusam -</p>
  <div class="hline" style="left:0;top:204px;width:21px"></div>
  <div class="hline" style="left:90px;top:204px;width:328px"></div>
  <div class="brand-stack" style="left:26px;top:180px">Bright<br>Towns<br>Alliance</div>
</section>

<!-- bullets -->
<section class="slide" style="left:462px;top:276px">
  <div class="photo" role="img" aria-label="Two climbers helping each other up a rock against a bright sky" style="left:0;top:0;width:174px;height:236px;background:linear-gradient(160deg,#2a2fc8 0%,#5b7fe0 40%,#a9bde8 60%,#6a4a3a 85%,#2a2220 100%)"></div>
  <div class="abs" style="left:174px;top:0;width:1.5px;height:236px;background:var(--orange)"></div>
  <div class="abs" style="left:396px;top:0;width:1.5px;height:236px;background:var(--orange)"></div>
  <h2 class="side-title">LOREM IPSUM DOLOR<br>SIT AMET</h2>
  <ul class="side-list">
    <li>Lorem ipsum dolor sit amet</li>
    <li>consetetur sadipscing elitr,</li>
    <li>sed diam eirmod tempor</li>
    <li>invidunt ut labore et dolore</li>
    <li>magna aliquyam erat sed</li>
  </ul>
  <div class="brand-line" style="top:211px">Bright Towns Alliance</div>
</section>

<!-- enhancements -->
<section class="slide" style="left:15px;top:526px">
  <div class="photo" role="img" aria-label="Night view of the earth with glowing connected city lights and location pins" style="left:0;top:0;width:418px;height:70px;background:linear-gradient(180deg,#0d1a33 0%,#27406e 55%,#6f8cc4 100%)"></div>
  <div class="hline" style="left:0;top:70px;width:418px"></div>
  <div class="col" style="left:82px">More<br>help for<br>cities</div>
  <div class="col" style="left:169px">More<br>visibility<br>for<br>sponsors</div>
  <div class="col" style="left:257px">More<br>data<br>about<br>cities</div>
  <div class="col" style="left:344px">More<br>time with<br>more<br>cities</div>
  <div class="tag">2018 ENHANCEMENTS</div>
  <div class="hline" style="left:0;top:204px;width:21px"></div>
  <div class="hline" style="left:90px;top:204px;width:328px"></div>
  <div class="brand-stack" style="left:26px;top:180px">Bright<br>Towns<br>Alliance</div>
</section>

<!-- appeal -->
<section class="slide" style="left:462px;top:526px">
  <div class="vline" style="left:22px;top:0;height:232px"></div>
  <p class="appeal">Please help us<br>help <b>cities &amp;<br>citizens</b></p>
  <div class="photo" role="img" aria-label="Laboratory scene with orange liquid being poured under a microscope" style="left:261px;top:0;width:157px;height:236px;background:linear-gradient(170deg,#8a8a86 0%,#d8d2cc 35%,#c9603a 60%,#5b6470 100%)"></div>
  <div class="vline" style="left:260px;top:0;height:236px"></div>
  <div class="brand-stack" style="left:11px;top:170px">Bright<br>Towns<br>Alliance</div>
</section>

<!-- market -->
<section class="slide" style="left:234px;top:783px">
  <div class="stat" style="left:18px;top:12px">
    <div class="fig">$757<small>bn</small></div><div class="when">by 2020</div>
    <ul style="top:48px"><li>19% CAGR (compound annual growth rate)</li><li>Trend &amp; Tally</li></ul>
  </div>
  <div class="stat" style="left:198px;top:12px">
    <div class="fig">$ 1.38<small>tn</small></div><div class="when">by 2020</div>
    <ul style="top:48px"><li>20% CAGR overall, 38% CAGR Asia-Pacific</li><li>Meridian Insight</li></ul>
  </div>
  <div class="stat" style="left:18px;top:106px">
    <div class="fig">$1.45<small>tn</small></div><div class="when">by 2020</div>
    <ul style="top:48px"><li>19% CAGR (compound annual growth rate)</li><li>Trend &amp; Tally</li></ul>
  </div>
  <div class="stat" style="left:198px;top:106px">
    <div class="fig">$41<small>tn</small></div>
    <ul style="top:48px"><li>20% CAGR overall, 38% CAGR Asia-Pacific</li><li>Meridian Insight</li></ul>
  </div>
  <div class="sheet-title">SMART CITIES MARKET SIZE</div>
  <div class="brand-stack" style="left:372px;top:199px;font-size:10px;line-height:9.5px">Bright<br>Towns<br>Alliance</div>
</section>

</body>
</html>
```